Fuel Your Day: Designing Eye-Catching Energy Ball Packaging

Here are the task requirements for my new project ENERGY BALLS under my existing baking business, Velvet_Crumb_by_Nora
Looking to create standout packaging that aligns with my brands fun and vibrant identity while allowing room for future growth and product line expansion.
1. Develop 3 Different Packaging Designs:
Create unique packaging for three different energy ball flavors to be launched initially.
2. Flexible Design for Future Modifications:
Ensure the packaging design is adaptable to accommodate new flavors or variations in the future. The initial 3 flavors are:
(i) Dates, Cashew & Chocolate
(ii) Dates, Cranberries & Oatmeal
(iii) Dates, Cashew & Ginger
3. Distinct Color Scheme for Each Flavor:
Use live and vibrant colors, (maybe flouro) with each flavor having its own distinct color.
4. Incorporate Key Ingredients on Packaging:
The front of each package should display the key ingredients for that specific flavor + an energy ball or not....
5. Fun Graphics of Ingredients:
Design graphics of the key ingredients that include fun, animated elements, such as faces, to create a playful and engaging look (similar to the attached graphics).
Looking to create standout packaging that aligns with my brand's fun and vibrant identity while allowing room for future growth and product line expansion.

```html
<!DOCTYPE html>
<html lang="en">
<head>
<meta charset="utf-8">
<title>Velvet Crumb by Nora — Energy Balls Packaging</title>
<link rel="stylesheet" href="https://fonts.googleapis.com/css2?family=Oswald:wght@400&family=Permanent+Marker&family=Gochi+Hand&display=swap">
<style>
  :root {
    --page: #ffffff;
    --cran-base: #d0197f;
    --cran-seal: #c4106f;
    --cran-band: #e0bb2c;
    --cran-brand: #ffffff;
    --cash-base: #ef8fd0;
    --cash-seal: #ea86c8;
    --cash-band: #d21a82;
    --cash-brand: #e4408f;
    --ink-light: #ffffff;
  }
  * { margin: 0; padding: 0; box-sizing: border-box; }
  html, body { width: 1200px; height: 800px; overflow: hidden; background: var(--page); }
  .stage { position: relative; width: 1200px; height: 800px; }

  .pouch {
    position: absolute; top: 81px; width: 390px; height: 635px;
    border-radius: 6px; overflow: hidden;
    background: var(--base);
  }
  .pouch--cranberry { left: 160px; --base: var(--cran-base); --seal: var(--cran-seal); --band: var(--cran-band); --brand: var(--cran-brand); --figure: linear-gradient(160deg, #d9897a, #b85a52); }
  .pouch--cashew { left: 613px; --base: var(--cash-base); --seal: var(--cash-seal); --band: var(--cash-band); --brand: var(--cash-brand); --figure: linear-gradient(160deg, #d6ad76, #a97c4a); }

  .pouch__seal {
    position: absolute; left: 0; top: 0; width: 100%; height: 100px;
    background: var(--seal);
    border-bottom: 3px solid rgba(0,0,0,0.08);
  }
  .pouch__zip { position: absolute; left: 14px; right: 14px; top: 86px; height: 3px; background: rgba(255,255,255,0.25); }

  .brand { position: absolute; left: 88px; top: 112px; display: flex; align-items: center; gap: 16px; }
  .brand__mark { width: 84px; height: 74px; background: var(--brand); border-radius: 4px; }
  .brand__name { font-family: "Oswald", sans-serif; font-weight: 400; color: var(--brand); line-height: 1; text-transform: uppercase; }
  .brand__name span { display: block; }
  .brand__line1 { font-size: 22px; letter-spacing: -0.5px; }
  .brand__line2 { font-size: 42px; margin-top: 4px; }

  .pouch__band {
    position: absolute; left: 0; top: 196px; width: 100%; height: 290px;
    background: var(--band);
    clip-path: polygon(0 8%, 20% 5%, 45% 9%, 70% 3%, 100% 1%, 100% 100%, 70% 97%, 40% 100%, 15% 96%, 0 98%);
  }

  .title {
    position: absolute; left: 28px; top: 196px; width: 340px;
    font-family: "Permanent Marker", cursive; color: var(--ink-light);
    text-transform: uppercase; line-height: 0.92; transform: rotate(-4deg);
  }
  .title__word { display: block; }
  .title__word--top { font-size: 82px; letter-spacing: -2px; }
  .title__word--bottom { font-size: 82px; margin-left: 36px; letter-spacing: -2px; }

  .mascot {
    position: absolute; left: 105px; top: 345px; width: 180px; height: 225px;
    border-radius: 46% 46% 42% 42%;
    background: var(--figure);
  }

  .flavor {
    position: absolute; left: 0; bottom: 26px; width: 100%; text-align: center;
    font-family: "Gochi Hand", cursive; font-size: 27px; color: var(--ink-light);
  }
</style>
</head>
<body>
<main class="stage">

  <section class="pouch pouch--cranberry" aria-label="Energy Balls — Dates, Cranberries and Oatmeal pouch">
    <div class="pouch__seal"><div class="pouch__zip"></div></div>
    <div class="brand">
      <div class="brand__mark"></div>
      <p class="brand__name"><span class="brand__line1">Velvet Crumb</span><span class="brand__line2">by Nora</span></p>
    </div>
    <div class="pouch__band"></div>
    <h1 class="title"><span class="title__word title__word--top">Energy</span><span class="title__word title__word--bottom">Balls</span></h1>
    <div class="mascot" role="img" aria-label="Cheerful cartoon date character with arms and legs"></div>
    <p class="flavor">Dates, Cranberries &amp; Oatmeal</p>
  </section>

  <section class="pouch pouch--cashew" aria-label="Energy Balls — Dates, Cashew and Chocolate pouch">
    <div class="pouch__seal"><div class="pouch__zip"></div></div>
    <div class="brand">
      <div class="brand__mark"></div>
      <p class="brand__name"><span class="brand__line1">Velvet Crumb</span><span class="brand__line2">by Nora</span></p>
    </div>
    <div class="pouch__band"></div>
    <h2 class="title"><span class="title__word title__word--top">Energy</span><span class="title__word title__word--bottom">Balls</span></h2>
    <div class="mascot" role="img" aria-label="Jumping cartoon cashew character with arms and legs"></div>
    <p class="flavor">Dates, Cashew &amp; Chocolate</p>
  </section>

</main>
</body>
</html>
```